Guinea Pigs and Budgerigars Stud card design

The stud name for our animals is "Tarrinja" We offer a service for stud cavies (guinea pigs) and offer show and pet stock for sale. We also have show and pet stock for sale for show budgerigars as well

The animals/birds we show are very beautiful and we are a very professional stud. Our property entrance is in Black so we would also like to reflect that in the card, with Tarrinja and all writing in black. We can supply 2 photos to be integrated into the card, one of a black guinea pig and one of a yellow budgerigar. Tarrinja also means 'place of many owls' so we would also like an owl (not a cartoon type, a natural looking owl, preferably an australian barn owl) integrated into the design as well :)
Updates

Please also add the website address to the design
http://www.tarrinjafarm.example

Target Market(s)

professional animal breeders and families new to the industry

Industry/Entity Type

Pet

Contact Information for Business Card

Tarrinja
Joanne Petrakis and Malcolm Varga
Mallowbrook Flat Qld
0417 628 903

Requirements
Must have
• card to integrate 2 photos plus an owl ( I will try to find an example pic)

```html
<!DOCTYPE html>
<html lang="en">
<head>
<meta charset="utf-8">
<title>Tarrinja – Stud Card</title>
<link rel="stylesheet" href="https://fonts.googleapis.com/css2?family=Cabin:wght@400;600;700&display=swap">
<style>
  :root {
    --ink: #000000;
    --paper: #ffffff;
    --reflection: #4a4a4a;
    --owl-light: #f1ece4;
    --owl-dark: #bfae98;
    --budgie-light: #f4ee7a;
    --budgie-deep: #e2d12c;
    --cavy-dark: #1c1c1f;
    --ribbon: #9a6fc1;
  }
  html, body {
    margin: 0;
    padding: 0;
    overflow: hidden;
    background: var(--paper);
  }
  .card {
    position: relative;
    width: 1200px;
    height: 707px;
    background: var(--ink);
    overflow: hidden;
    font-family: "Cabin", "Trebuchet MS", sans-serif;
    color: var(--ink);
  }
  .card__panel {
    position: absolute;
    left: 53px;
    top: 55px;
    width: 1093px;
    height: 596px;
    background: var(--paper);
  }

  /* Wordmark and its mirrored reflection */
  .stud-name,
  .stud-name-reflection {
    position: absolute;
    left: 98px;
    top: 99px;
    margin: 0;
    font-size: 135px;
    font-weight: 400;
    line-height: 1;
    letter-spacing: -1px;
    white-space: nowrap;
  }
  .stud-name { z-index: 2; }
  .stud-name-reflection {
    z-index: 1;
    color: var(--reflection);
    transform-origin: 0 120px;
    transform: scaleY(-1);
    -webkit-mask-image: linear-gradient(to top, transparent 0%, transparent 11%, rgba(0,0,0,0.6) 12%, transparent 62%);
            mask-image: linear-gradient(to top, transparent 0%, transparent 11%, rgba(0,0,0,0.6) 12%, transparent 62%);
    pointer-events: none;
    user-select: none;
  }

  .owl-art {
    position: absolute;
    z-index: 3;
    left: 172px;
    top: 60px;
    width: 258px;
    height: 64px;
    border-radius: 50% 50% 45% 45% / 80% 80% 20% 20%;
    background: radial-gradient(ellipse at 50% 65%, var(--owl-light) 0%, var(--owl-dark) 100%);
  }

  .photo-frame {
    position: absolute;
    box-sizing: border-box;
    margin: 0;
    border-style: solid;
    border-color: var(--ink);
    background: var(--paper);
    z-index: 2;
  }
  .photo-frame--budgie {
    left: 80px;
    top: 293px;
    width: 222px;
    height: 294px;
    border-width: 8px;
  }
  .photo-frame--cavy {
    left: 712px;
    top: 168px;
    width: 404px;
    height: 352px;
    border-width: 10px;
  }
  .photo {
    width: 100%;
    height: 100%;
  }
  .photo--budgie {
    background: radial-gradient(ellipse at 45% 60%, var(--budgie-deep) 0%, var(--budgie-light) 35%, var(--paper) 70%);
  }
  .photo--cavy {
    background: linear-gradient(160deg, var(--ribbon) 0%, var(--ribbon) 30%, var(--cavy-dark) 55%, var(--cavy-dark) 85%, var(--paper) 100%);
  }

  .contact {
    position: absolute;
    z-index: 2;
    left: 305px;
    top: 290px;
    width: 400px;
    text-align: center;
    font-weight: 700;
  }
  .contact__names {
    margin: 0;
    font-size: 24px;
    line-height: 36px;
  }
  .contact__line {
    margin: 0;
    font-size: 22px;
    line-height: 40px;
  }
  .contact__names + .contact__line { margin-top: 14px; }

  .tagline {
    position: absolute;
    left: 53px;
    width: 1093px;
    top: 612px;
    margin: 0;
    text-align: center;
    font-size: 32px;
    font-weight: 400;
    line-height: 1;
  }
</style>
</head>
<body>
  <main class="card">
    <div class="card__panel"></div>

    <h1 class="stud-name">Tarrinja</h1>
    <div class="stud-name-reflection" aria-hidden="true">Tarrinja</div>
    <div class="owl-art" role="img" aria-label="Natural barn owl in flight with wings spread"></div>

    <figure class="photo-frame photo-frame--budgie">
      <div class="photo photo--budgie" role="img" aria-label="Photo of a yellow exhibition budgerigar perched on a branch"></div>
    </figure>

    <figure class="photo-frame photo-frame--cavy">
      <div class="photo photo--cavy" role="img" aria-label="Photo of a black pedigree cavy under a purple champion ribbon"></div>
    </figure>

    <section class="contact">
      <p class="contact__names">Joanne Petrakis<br>and<br>Malcolm Varga</p>
      <p class="contact__line">Mallowbrook Flat Qld 0417 628 903</p>
      <p class="contact__line">Phone #: 0482736154</p>
      <p class="contact__line">http://www.tarrinjafarm.example</p>
    </section>

    <p class="tagline">Breeders of Exhibition Budgerigars and Pedigree Cavies</p>
  </main>
</body>
</html>
```